Tessarin - A/B testing for professionals

We need to improve the presentation layer (design only) of our tool zentiva-ab.net.

www.zentiva-ab.net is a A/B testing tool for websites and all kind of applications. The most important features are already listed on our actual webpage and the attached screenshots.
the animated icons on the front page should be included into the design and should match the color scheme. if you think you need to add a logo or similar things to it - feel free to offer us good proposals. you can reach us by sending us a mail to: support@zentiva-ab.net

our needs listed:
-we'd rather have a very good improvement of the actual design instead of a big redesign with all colours changed etc.
- the pages in the screenshots attached should be redesigned. The amount of different layouts will be around 2 - 4 depending on the design.
- the animated icons on www.zenntiva-ab.net must be included into the design.
- the colors should match with the animated icons.
- we won't need any code. Psd / ai / graphic files only.

Target Market(s)

everyone who sells something with their webpage / application.

Number of Pages Required

3 page

Colors
85cae6
3276b5
85abd2
cee9f5
eaf1f7
0455a3
000000
0492cd

Requirements
Must have
• - animated icons included on the main page.
• - color match with the animated icons on our website or good proposal for adjusting them accordingly.
• - touch of that is highly scaleable and adjustable: we invented a new query language for the project
• - sweetness of the modern web projects and libraries
• - touch that the date are not shared between different users - high value on privacy
Nice to have
• - proposal for a matching logo or including the actual properly
Should not have
• - images people in the design
• - coded versions

```html
<!DOCTYPE html>
<html lang="en">
<head>
<meta charset="utf-8">
<title>Tessarin – Contact</title>
<link href="https://fonts.googleapis.com/css2?family=Open+Sans:wght@300;400;600;700&display=swap" rel="stylesheet">
<style>
  :root {
    --backdrop: #ececec;
    --page: #ffffff;
    --header-bg: #f8f8f8;
    --brand: #3aa7c4;
    --link: #3aa7c4;
    --text: #555a5e;
    --muted: #9a9fa3;
    --field-border: #e3e5e7;
    --accent-border: #a9dcea;
    --footer-bg: #333333;
    --footer-text: #ffffff;
  }
  * { box-sizing: border-box; margin: 0; padding: 0; }
  html, body {
    width: 1200px; height: 1200px; overflow: hidden;
    background: var(--backdrop);
    font-family: "Open Sans", Arial, sans-serif;
  }
  .site {
    position: absolute; left: 0; top: 365px;
    width: 1200px; height: 470px;
    background: var(--page);
  }
  .site-header {
    position: absolute; left: 0; top: 0; width: 1200px; height: 40px;
    background: var(--header-bg);
  }
  .brand {
    position: absolute; left: 214px; top: 6px;
    font-size: 19px; font-weight: 700; letter-spacing: 1.5px;
    color: var(--brand); text-transform: uppercase;
  }
  .nav-install {
    position: absolute; left: 877px; top: 12px;
    font-size: 10px; letter-spacing: 0.6px; color: var(--text);
  }
  .btn {
    position: absolute; border: 2px solid var(--accent-border); border-radius: 4px;
    font-size: 10px; letter-spacing: 0.8px; color: var(--text);
    display: flex; align-items: center; justify-content: center; background: transparent;
  }
  .btn-login { left: 924px; top: 6px; width: 60px; height: 23px; }
  .intro { position: absolute; left: 215px; top: 88px; color: var(--text); font-weight: 300; }
  .intro h1 { font-size: 21px; font-weight: 400; letter-spacing: 1px; line-height: 26px; }
  .intro p { font-size: 12px; letter-spacing: 0.6px; line-height: 15px; }
  .intro .gap { margin-top: 14px; }
  .intro a { color: var(--link); text-decoration: none; }
  .field {
    position: absolute; border: 2px solid var(--field-border); border-radius: 4px;
    font-size: 6.5px; color: var(--muted); padding: 6px 0 0 16px; letter-spacing: 0.3px;
  }
  .field-name { left: 216px; top: 206px; width: 124px; height: 24px; }
  .field-email { left: 216px; top: 237px; width: 124px; height: 24px; }
  .field-subject { left: 216px; top: 267px; width: 124px; height: 24px; }
  .field-message { left: 360px; top: 206px; width: 168px; height: 85px; padding-left: 11px; }
  .btn-send { left: 468px; top: 298px; width: 60px; height: 23px; }
  .site-footer {
    position: absolute; left: 0; top: 361px; width: 1200px; height: 109px;
    background: var(--footer-bg); color: var(--footer-text);
  }
  .footer-brand {
    position: absolute; left: 215px; top: 13px;
    font-size: 11.5px; font-weight: 700; letter-spacing: 1px; text-transform: uppercase;
  }
  .footer-col { position: absolute; top: 38px; font-size: 6.5px; line-height: 15.2px; }
  .footer-col h2 { font-size: 6.5px; font-weight: 600; letter-spacing: 0.4px; }
  .footer-col ul { list-style: none; }
  .col-docs { left: 215px; }
  .col-info { left: 296px; }
  .col-about { left: 378px; }
  .social { position: absolute; left: 952px; top: 15px; }
  .copyright {
    position: absolute; right: 214px; top: 82px;
    font-size: 6.5px; font-weight: 600; letter-spacing: 0.3px;
  }
</style>
</head>
<body>
  <div class="site">
    <header class="site-header">
      <div class="brand">Tessarin</div>
      <div class="nav-install">INSTALL</div>
      <div class="btn btn-login">LOGIN</div>
    </header>

    <section class="intro">
      <h1>CONTACT US.</h1>
      <p>We are happy to help you out.</p>
      <p>Before contacting us, you might consider <a href="#">asking a question</a> first.</p>
      <p>There is also our <a href="#">documentation</a> which might help you out.</p>
      <p class="gap">For every other case, feel free to contact us.</p>
    </section>

    <form class="contact-form">
      <div class="field field-name">NAME</div>
      <div class="field field-email">EMAIL</div>
      <div class="field field-subject">SUBJECT</div>
      <div class="field field-message">MASSAGE</div>
      <div class="btn btn-send">SEND</div>
    </form>

    <footer class="site-footer">
      <div class="footer-brand">Tessarin</div>
      <nav class="footer-col col-docs">
        <h2>DOKUMENTATION</h2>
        <ul><li>Guides</li><li>Query Docs</li><li>Report Docs</li></ul>
      </nav>
      <nav class="footer-col col-info">
        <h2>INFORMATION</h2>
        <ul><li>Ask Questions</li><li>Answer Questions</li><li>Official Blog</li></ul>
      </nav>
      <nav class="footer-col col-about">
        <h2>ABOUT</h2>
        <ul><li>Privacy</li><li>Contact</li><li>About us</li></ul>
      </nav>
      <svg class="social" width="34" height="14" viewBox="0 0 34 14" aria-label="Social links">
        <circle cx="6" cy="7" r="5.5" fill="none" stroke="#ffffff" stroke-width="1"/>
        <circle cx="24" cy="7" r="5.5" fill="none" stroke="#ffffff" stroke-width="1"/>
      </svg>
      <div class="copyright">© TESSARIN, 2015</div>
    </footer>
  </div>
</body>
</html>
```